TOLO Electrical Services Letter Head

I need a professional clean looking design that will incorporate my company logo and information such as postal address, website, contact email "service@tolovoltworks.com.au" and phone number.

somewhere on the document i will also require my electrical contractor number "EC 046215" and my Australian Business number "57 139 604 282" these have to legally be on the document so they dont need to be a main feature, maybe in the footer in a smaller text.

Can you also have the 3 blue dashes from my logo as the watermark.

I would like the colour scheme to match my logo, business card and website www.tolovoltworks.com.au

I have the JPEG and PNG files for my logo which it will not allow me to upload as they are too wide, if you require these please let me know.

Target Market(s)

To be used for quotes and letters to commercial clients

Industry/Entity Type

Electric Company

Colors
0555a3
3176b5
85acd3
cfdfed
eaf1f7

Requirements
Must have
• company logo and information such as postal address, website, contact email "service@tolovoltworks.com.au" and phone number.
• somewhere on the document i will also require my electrical contractor number "EC 046215" and my Australian Business number "57 139 604 282" these have to legally be on the document so they dont need to be a main feature, maybe in the footer in a smaller text.
• I would like the colour scheme to match my logo, business card and website www.tolovoltworks.com.au
Nice to have
• Can you also have the 3 blue dashes from my logo as the watermark.

```html
<!DOCTYPE html>
<html lang="en">
<head>
<meta charset="utf-8">
<title>TOLO Electrical Services Letterhead</title>
<link rel="stylesheet" href="https://fonts.googleapis.com/css2?family=Open+Sans:wght@400;700&family=EB+Garamond:wght@400&display=swap">
<style>
  :root {
    --backdrop: #ddd0b9;
    --paper: #ffffff;
    --brand-deep: #0555a3;
    --brand-mid: #3176b5;
    --brand-soft: #85acd3;
    --brand-pale: #cfdfed;
    --brand-mist: #eaf1f7;
    --ink: #4a4a4a;
    --ink-dark: #1a1f33;
  }
  * { margin: 0; padding: 0; box-sizing: border-box; }
  html, body { width: 1200px; height: 900px; overflow: hidden; }
  body { background: var(--backdrop); position: relative; }
  .letterhead {
    position: absolute; left: 300px; top: 26px;
    width: 600px; height: 848px;
    background: var(--paper);
    box-shadow: 0 6px 18px rgba(0,0,0,.12);
    overflow: hidden;
  }
  .letterhead__shapes { position: absolute; inset: 0; }
  .brand {
    position: absolute; right: 22px; top: 14px; text-align: right;
  }
  .brand__name {
    font-family: "Open Sans", sans-serif; font-weight: 700;
    font-size: 13px; color: var(--ink-dark); letter-spacing: .2px;
  }
  .brand__legal {
    font-family: "EB Garamond", serif; font-size: 11px;
    color: var(--ink-dark); line-height: 1.1; margin-top: 2px;
  }
  .watermark {
    position: absolute; left: 0; right: 0; top: 300px; text-align: center;
    font-family: "Open Sans", sans-serif; font-weight: 700;
    font-size: 96px; color: var(--brand-mist); letter-spacing: 8px;
  }
  .letter-body {
    position: absolute; left: 70px; right: 70px; top: 250px;
    font-family: "Open Sans", sans-serif; font-size: 8.6px;
    line-height: 1.6; color: var(--ink);
  }
  .letter-body p { margin-bottom: 14px; }
  .sign-off {
    position: absolute; right: 78px; top: 520px;
    font-family: "Open Sans", sans-serif; font-size: 8px; color: var(--ink);
  }
  .signature {
    position: absolute; right: 60px; top: 540px; width: 80px; height: 60px;
  }
  .footer-address {
    position: absolute; left: 20px; bottom: 14px;
    font-family: "EB Garamond", serif; font-size: 12px; color: var(--ink-dark);
  }
  .footer-contact {
    position: absolute; right: 20px; bottom: 22px; text-align: right;
    font-family: "EB Garamond", serif; font-size: 11.5px;
    line-height: 1.05; color: var(--ink-dark);
  }
</style>
</head>
<body>
  <article class="letterhead">
    <svg class="letterhead__shapes" width="600" height="848" viewBox="0 0 600 848" aria-hidden="true">
      <defs>
        <linearGradient id="band-footer" x1="0" y1="1" x2="1" y2="0">
          <stop offset="0" stop-color="#0555a3"/>
          <stop offset="1" stop-color="#2a9bd8"/>
        </linearGradient>
      </defs>
      <path d="M0,0 H600 V6 C430,28 190,52 0,112 Z" fill="var(--brand-mid)"/>
      <path d="M0,0 H600 C430,20 180,40 0,96 Z" fill="var(--brand-deep)"/>
      <path d="M600,520 C560,640 330,690 170,700 C90,705 30,730 0,780 V848 H600 Z" fill="var(--brand-soft)"/>
      <path d="M600,536 C565,650 340,702 180,712 C95,717 35,742 0,792 V848 H600 Z" fill="url(#band-footer)"/>
    </svg>

    <header class="brand">
      <div class="brand__name">TOLO Electrical Services</div>
      <div class="brand__legal">Aus Business # 57 139 604 282<br>EC 046215</div>
    </header>

    <div class="watermark" aria-hidden="true">TOLO</div>

    <section class="letter-body">
      <p>Lorem ipsum dolor sit amet, consectetur adipiscing elit. Donec orci purus, luctus vitae dignissim eu, iaculis sed purus. Vivamus faucibus, ipsum nec aliquet viverra, leo mauris condimentum ligula, sit amet sagittis enim ligula quis arcu. Nam egestas tortor id nisi porttitor mattis. In tortor ante, ultricies in suscipit a, tempus non massa. Vivamus et auctor mi. Fusce vel massa nulla. Phasellus nec eros mauris, et scelerisque orci.</p>
      <p>Donec malesuada orci vitae nulla accumsan porta a id massa. Quisque accumsan iaculis magna sit amet fringilla. Maecenas consequat, magna eget tincidunt semper, odio nibh rutrum mi, id feugiat ante nisi eu risus. Vestibulum nunc orci, rhoncus a placerat in, ultricies in mi. Cras mattis varius eros, vel fringilla nisi suscipit eget. Quisque scelerisque sagittis nulla at porttitor.</p>
      <p>Sed id augue vitae urna euismod commodo aliquet a quam. Pellentesque arcu velit, cursus et malesuada ut, consequat et diam. Nullam erat sem, rhoncus id ullamcorper vitae, rhoncus et arcu. In ultricies ultricies nulla, ut rutrum nisi iaculis at. Donec eu magna a metus ornare faucibus. Fusce aliquet faucibus ultricies. Morbi semper, est id tincidunt gravida, sem arcu adipiscing lacus, ac bibendum nulla leo eu purus. Quisque nec diam sed risus consectetur accumsan quis quis nibh. Vestibulum id purus lorem.</p>
    </section>

    <div class="sign-off">Sincerely,</div>
    <svg class="signature" viewBox="0 0 80 60" role="img" aria-label="Handwritten signature with company stamp">
      <circle cx="30" cy="34" r="22" fill="none" stroke="var(--brand-soft)" stroke-width="2"/>
      <rect x="36" y="12" width="38" height="26" fill="var(--brand-pale)" opacity=".6"/>
    </svg>

    <footer>
      <div class="footer-address">Sample Address Sample Street</div>
      <div class="footer-contact">
        Tel: 123-555-984<br>
        Mob: 123-456-78<br>
        Fax: 123-456-78<br>
        Email: service@tolovoltworks.com.au<br>
        www.tolovoltworks.com.au
      </div>
    </footer>
  </article>
</body>
</html>
```